Business Card Design Project

We need a simple business card design that uses our current logo.
We need to have the current logo put into a high res format.
We need to have 1 card made with contact information.
We will supply the information for the 4 employees.
Industry/Entity Type
Business
Requirements
Must have
- The contact information is as follows:
Paul Vardenko
Producer/CEO
c. 949-555-0148
f. 650-555-0193
paulv@lanternyardstudio.example
Mel Trosgaard, CFO
c. 949-555-0172
f. 650-555-0193
melt@lanternyardstudio.example
Paul Brenneky, PR
c. 267-555-0126
f. 650-555-0193
pbrenneky@lanternyardstudio.example
Dale Furnow, Producer
c. 949-555-0164
f. 650-555-0193
dalef@lanternyardstudio.example
The address for all cards is:
318 W Calle Norvista #2715, San Clemente, CA 92631

```html
<!DOCTYPE html>
<html lang="en">
<head>
<meta charset="utf-8">
<title>Lantern Yard Studio — Business Card</title>
<link rel="stylesheet" href="https://fonts.googleapis.com/css2?family=Jost:wght@400;500&display=swap">
<style>
  :root {
    --page-bg: #ffffff;
    --card-dark: #0c0c0c;
    --card-mid: #262626;
    --card-glow: #5a5a5a;
    --decor-band: #1a1a1a;
    --decor-edge: #101010;
    --text-soft: #c9c9c9;
    --text-dim: #bdbdbd;
    --brand-blue: #4fb2e8;
  }
  * { margin: 0; padding: 0; box-sizing: border-box; }
  html, body {
    width: 1200px;
    height: 960px;
    overflow: hidden;
    background: var(--page-bg);
    font-family: "Jost", "Futura", sans-serif;
  }
  .business-card {
    position: absolute;
    left: 188px;
    top: 270px;
    width: 804px;
    height: 458px;
    overflow: hidden;
    background:
      radial-gradient(ellipse 520px 420px at 680px 430px, var(--card-glow) 0%, var(--card-mid) 55%, var(--card-dark) 100%);
  }
  .decor-area {
    position: absolute;
    left: 22px;
    top: 0;
    width: 408px;
    height: 458px;
    background: linear-gradient(90deg, var(--decor-edge) 0%, var(--decor-band) 50%, rgba(26, 26, 26, 0) 100%);
    opacity: 0.7;
  }
  .contact-block {
    position: absolute;
    right: 44px;
    top: 72px;
    text-align: right;
    color: var(--text-soft);
  }
  .contact-name {
    font-size: 24px;
    letter-spacing: 3px;
    line-height: 32px;
    font-weight: 400;
    text-transform: uppercase;
  }
  .contact-title {
    font-size: 22px;
    letter-spacing: 3px;
    line-height: 30px;
    margin-bottom: 10px;
    text-transform: uppercase;
  }
  .contact-line {
    font-size: 22px;
    letter-spacing: 3px;
    line-height: 27px;
    color: var(--text-dim);
  }
  .contact-line.email { letter-spacing: 1.5px; }
  .brand-name {
    position: absolute;
    right: 40px;
    top: 364px;
    font-size: 34px;
    font-weight: 500;
    line-height: 40px;
    color: var(--brand-blue);
  }
  .address-line {
    position: absolute;
    right: 34px;
    top: 416px;
    font-size: 21px;
    line-height: 26px;
    color: var(--text-dim);
  }
</style>
</head>
<body>
  <section class="business-card" aria-label="Business card for Mel Trosgaard, Lantern Yard Studio">
    <div class="decor-area" role="img" aria-label="Faint repeated vertical company name pattern"></div>

    <div class="contact-block">
      <p class="contact-name">Mel Trosgaard</p>
      <p class="contact-title">CFO</p>
      <p class="contact-line">c. 949-555-0172</p>
      <p class="contact-line">f. 650-555-0193</p>
      <p class="contact-line email">melt@lanternyardstudio.example</p>
    </div>

    <p class="brand-name">Lantern Yard Studio</p>
    <p class="address-line">318 W Calle Norvista #2715, San Clemente, CA 92631</p>
  </section>
</body>
</html>
```